Flyer Design

We are a property company and need attractive flyers that will grab peoples attention. We want them to be bold but simple and not too busy. I attach a draft and also our logo. We will print in A5 size.
Thank you & I look forward to receiving designs.

Industry/Entity Type

It Company

```html
<!DOCTYPE html>
<html lang="en">
<head>
<meta charset="utf-8">
<title>Nori Developments Flyer</title>
<link rel="stylesheet" href="https://fonts.googleapis.com/css2?family=Cinzel:wght@400;700&family=Crimson+Text:wght@600;700&display=swap">
<style>
  :root {
    --page-bg: #8a8a8a;
    --wood-dark: #3e2c20;
    --wood-mid: #7a5f48;
    --wood-light: #b39a80;
    --shutter: #e6d8c6;
    --light-core: #f6eddc;
    --plum: #5c3a45;
    --rose: #b07a62;
    --gold-brown: #6e4c2c;
    --oxblood: #3d1717;
    --cream: #fbf4ea;
  }
  html, body {
    margin: 0;
    width: 1088px;
    height: 1200px;
    overflow: hidden;
    background: var(--page-bg);
  }
  .flyer {
    position: absolute;
    left: 134px;
    top: 20px;
    width: 820px;
    height: 1160px;
    overflow: hidden;
    box-shadow: 0 4px 18px rgba(0,0,0,0.35);
  }
  .flyer__stump {
    position: absolute;
    inset: 0;
    background:
      radial-gradient(ellipse 62% 40% at 50% 55%, var(--light-core) 0%, rgba(240,224,200,0.85) 40%, rgba(200,170,140,0) 75%),
      linear-gradient(180deg, #c9b59c 0%, #d9c4a8 50%, var(--rose) 80%, var(--plum) 100%);
  }
  .flyer__house {
    position: absolute;
    left: 0;
    top: 0;
    width: 100%;
    height: 520px;
    background:
      linear-gradient(180deg, rgba(0,0,0,0) 55%, rgba(217,196,168,0.9) 100%),
      linear-gradient(90deg, var(--wood-dark) 0%, var(--wood-mid) 14%, var(--wood-light) 40%, var(--wood-mid) 58%, var(--wood-mid) 100%);
  }
  .flyer__window {
    position: absolute;
    left: 436px;
    top: 50px;
    width: 310px;
    height: 256px;
    background: linear-gradient(90deg, var(--shutter) 0 24%, #c8b6a2 24% 76%, var(--shutter) 76% 100%);
    opacity: 0.85;
  }
  .flyer__content {
    position: absolute;
    inset: 0;
    text-align: center;
  }
  .logo-mark {
    position: absolute;
    left: 364px;
    top: 338px;
    width: 92px;
    height: 92px;
    background: rgba(110,76,44,0.75);
  }
  .wordmark {
    position: absolute;
    top: 466px;
    left: 0;
    right: 0;
    margin: 0;
    font-family: "Cinzel", serif;
    font-weight: 400;
    font-size: 50px;
    letter-spacing: 1px;
    color: var(--gold-brown);
  }
  .rule {
    position: absolute;
    left: 70px;
    right: 70px;
    height: 1px;
    background: rgba(110,76,44,0.35);
  }
  .rule--top { top: 548px; }
  .rule--mid { top: 772px; }
  .headline {
    position: absolute;
    left: 0;
    right: 0;
    margin: 0;
    font-family: "Cinzel", serif;
    font-weight: 700;
    font-size: 34px;
    line-height: 47px;
  }
  .headline--question { top: 568px; color: var(--gold-brown); }
  .headline--mortgage { top: 790px; color: var(--oxblood); font-size: 35px; line-height: 48px; }
  .tagline {
    position: absolute;
    top: 914px;
    left: 0;
    right: 0;
    margin: 0;
    font-family: "Crimson Text", serif;
    font-weight: 700;
    font-size: 22px;
    line-height: 28px;
    color: var(--oxblood);
  }
  .contact {
    position: absolute;
    left: 60px;
    top: 993px;
    width: 702px;
    height: 134px;
    border: 1px solid rgba(251,244,234,0.8);
    outline: 1px solid rgba(251,244,234,0.6);
    outline-offset: -6px;
    box-sizing: border-box;
    color: var(--cream);
    font-family: "Crimson Text", serif;
    font-weight: 600;
  }
  .contact__call {
    margin: 6px 0 0;
    font-weight: 700;
    font-size: 29px;
    line-height: 34px;
  }
  .contact__note {
    margin: 0;
    font-size: 17px;
    line-height: 21px;
  }
  .contact__web {
    margin: 5px 0 0;
    font-weight: 700;
    font-size: 20px;
  }
</style>
</head>
<body>
  <main class="flyer">
    <div class="flyer__stump" role="img" aria-label="Sepia cracked tree-stump cross-section glowing with warm light, fading to plum at the bottom"></div>
    <div class="flyer__house" role="img" aria-label="Sepia photograph of a weathered wooden house wall with a wooden staircase on the left">
      <div class="flyer__window" role="img" aria-label="Window with open shutters and blinds"></div>
    </div>
    <div class="flyer__content">
      <span class="logo-mark" aria-hidden="true"></span>
      <h1 class="wordmark">Nori Developments</h1>
      <div class="rule rule--top"></div>
      <h2 class="headline headline--question">ARE YOU A HOMEOWNER<br>LOOKING FOR FINANCIAL FREEDOM<br>WHILE BEEN ABLE TO KEEP YOUR<br>OWN HOME?</h2>
      <div class="rule rule--mid"></div>
      <h2 class="headline headline--mortgage">ARE YOU STRUGGLING TO PAY<br>YOUR MORTGAGE?</h2>
      <p class="tagline">NORI SPECIALISE IN SUBDIVISIONS INCLUDING<br>FINANCE AND MANAGEMENT.</p>
      <section class="contact">
        <p class="contact__call">CALL 021 555 0147</p>
        <p class="contact__note">or email hello@norisubdivisions.com for more information or to find out<br>if your property is suitable for subdivision in Auckland.</p>
        <p class="contact__web">www.norisubdivisions.com</p>
      </section>
    </div>
  </main>
</body>
</html>
```